EVENT TENT DESIGN/ Revamping our Bi-fold Brochure/ Creating Tri Fold Brochure

Hello, I uploaded a pdf that shows the breakdown of our current brochure. We are having a hard time getting the colors correct. We want the front and back as well as any other gradient areas to be closer to our colors on the "Lumera Color Code and Font" document we uploaded.

We also feel like the solar images, outdated or the colors are a little too dull. We want more modern images with panels that are black on black or very very very navy/black blue worst case scenario.

In addition, we feel as the though some of the fonts and banners feel a little basic.

We are looking for somebody to add that modern feel to the brochure as well as turn the information into a trifold.

I will be uploading the brand page with colors and fonts, our logo, and the current book we have made. thank you in advance.

Lastly we need a "Refer a Friend" Page in the brochure. Please use the below link for inspiration. We are currently running a promo on our website, on our Brochure we like the referral pay out as follows.
https://www.trykelvaraenergy.com/refer-a-friend
You receive $35 for each qualified friend. Your qualified friend will get $25.
Get $500 when they go solar; $250 when they get a new roof.!

here is a link to our website. www.trykelvaraenergy.com
______________________________________________

Hello I increased the Winnings so that i can increase the scope of the project. I am uploading the tent measurements and a base template for you to work with. If you are a designer and have already created a Brochure for me and your design hasn't been deleted that means you are in the running for the winnings. I would like you to apply those elements to the tent design.

If you are a new designer. Use the elements that i want for the brochure and trifold and apply that to a Tent design.

my goal is to pick a designer by EOBD Thursday Aug 24th, 2023. Thank you
Updates

Colors
E54698
E96AAD
F1A4CE
F9D9EA
FCEFF6
A7469A
B969AE
D3A5CF
EDDBEB
F8F0F9
6B429C
8869AF
B7A5CE
E3DAEB
F3F0F8

Requirements
Must have
• Bi Fold Brochure Design, Tri-Fold Brochure, Event Tent Design

```html
<!DOCTYPE html>
<html lang="en">
<head>
<meta charset="utf-8">
<title>Lumera Brochure Cover</title>
<link rel="stylesheet" href="https://fonts.googleapis.com/css2?family=Montserrat:wght@300;400;800;900&display=swap">
<style>
  :root {
    --stage: #c9c9c9;
    --cover: #1d2a2e;
    --cover-edge: #172226;
    --magenta: #c018cc;
    --white: #ffffff;
    --muted: #c9d0d2;
    --photo-warm: #e8a234;
    --photo-mid: #7b5a3a;
    --photo-cool: #2b3c5c;
  }
  * { margin: 0; padding: 0; box-sizing: border-box; }
  html, body {
    width: 1200px;
    height: 900px;
    overflow: hidden;
    background: var(--stage);
  }
  .cover {
    position: absolute;
    left: 303px;
    top: 30px;
    width: 594px;
    height: 840px;
    background: var(--cover);
    overflow: hidden;
    font-family: "Montserrat", sans-serif;
  }
  .cover-art {
    position: absolute;
    inset: 0;
  }
  .brand {
    position: absolute;
    left: 88px;
    top: 62px;
    width: 260px;
    text-align: center;
    color: var(--white);
  }
  .brand-mark {
    display: inline-block;
    width: 34px;
    height: 34px;
    border-radius: 50%;
    background: var(--magenta);
    margin-bottom: 8px;
  }
  .brand-name {
    font-size: 26px;
    font-weight: 400;
    letter-spacing: 6px;
    line-height: 1;
  }
  .brand-tagline {
    margin-top: 6px;
    font-size: 8px;
    font-weight: 400;
    letter-spacing: 1.6px;
    color: var(--muted);
  }
  .headline {
    position: absolute;
    left: 44px;
    bottom: 90px;
  }
  .headline-lead {
    font-size: 27px;
    font-weight: 300;
    color: var(--white);
    letter-spacing: 0.5px;
    line-height: 1.1;
  }
  .headline-main {
    font-size: 58px;
    font-weight: 900;
    color: var(--magenta);
    line-height: 1;
    letter-spacing: 0.5px;
  }
</style>
</head>
<body>
  <main class="cover">
    <svg class="cover-art" width="594" height="840" viewBox="0 0 594 840" aria-hidden="false">
      <defs>
        <linearGradient id="photoTone" x1="1" y1="0" x2="0" y2="1">
          <stop offset="0" stop-color="var(--photo-warm)"/>
          <stop offset="0.35" stop-color="var(--photo-mid)"/>
          <stop offset="1" stop-color="var(--photo-cool)"/>
        </linearGradient>
      </defs>
      <path class="hero-photo" role="img"
            aria-label="Aerial photo of suburban homes with black rooftop solar panels at sunset"
            d="M96 178 L594 120 L594 455 Q450 590 96 602 Z"
            fill="url(#photoTone)"/>
      <path class="hero-arc" d="M96 612 Q470 600 594 440"
            fill="none" stroke="var(--magenta)" stroke-width="14" stroke-linecap="round"/>
    </svg>

    <div class="brand">
      <span class="brand-mark"></span>
      <div class="brand-name">LUMERA</div>
      <div class="brand-tagline">SOLAR | ROOFING | CONSTRUCTION</div>
    </div>

    <h1 class="headline">
      <span class="headline-lead">POWERING YOUR HOME WITH A</span><br>
      <span class="headline-main">BRIGHT FUTURE!</span>
    </h1>
  </main>
</body>
</html>
```